Label Design for a New Alcoholized Root Beer

Create a design for a new alcoholized root beer. This is a new product category in the USA growing very rapidly. Root Beer is a popular flavor of Cola, but recently, beer manufacturers have added alcohol to it and have created a new product that has gained traction on the market at a tremendous rate.

Root Beer is vintage product that has been around for a hundred years. Consumers of this product are mostly male between the age of 30 to 45. They purchase this product for its nostalgia and vintage look and taste.

This product will be in a standard 355 mL brown bottle.

It is 5.9% abv.

The name of the product is ''Osric's Hard Root Beer''.

We have uploaded some pictures of traditional root beers to give you an idea of the feel we want our product to have and also, the bottle the product will be filled in.

Target Market(s)

Consumers are male 30-45, same market as craft beer consumers

Industry/Entity Type

Product

Requirements
Must have
• Design must have a vintage feel to it

```html
<!DOCTYPE html>
<html lang="en">
<head>
<meta charset="utf-8">
<title>Osric's Hard Root Beer – Label</title>
<link rel="stylesheet" href="https://fonts.googleapis.com/css2?family=Alfa+Slab+One&family=Lobster&family=Open+Sans:wght@300;400&family=Playfair+Display:ital@1&display=swap">
<style>
  :root {
    --page: #ffffff;
    --label-cream: #fbf6f1;
    --ray-peach: #f8d6bf;
    --border-orange: #ef8a63;
    --ribbon-orange: #f08966;
    --ribbon-shade: #d9714f;
    --ink: #4a4644;
    --ink-soft: #8a8480;
  }
  html, body {
    margin: 0;
    padding: 0;
    width: 1200px;
    height: 1002px;
    overflow: hidden;
    background: var(--page);
  }
  .canvas {
    position: relative;
    width: 1200px;
    height: 1002px;
  }
  .label-art {
    display: block;
    width: 1200px;
    height: 1002px;
  }
  .label-body { fill: var(--label-cream); stroke: var(--border-orange); stroke-width: 16; }
  .label-inner-rule { fill: none; stroke: var(--border-orange); stroke-width: 2.5; }
  .sunburst { fill: url(#sunburstGlow); }
  .star { fill: var(--ink); }
  .flourish { fill: var(--ink); opacity: 0.2; }
  .ribbon-band { fill: var(--ribbon-orange); }
  .ribbon-tail { fill: var(--ribbon-orange); }
  .ribbon-fold { fill: var(--ribbon-shade); }
  .rule { stroke: var(--ink); stroke-width: 2; }

  .kicker {
    font-family: "Alfa Slab One", serif;
    font-size: 27px;
    letter-spacing: 3px;
    fill: var(--ink);
  }
  .category {
    font-family: "Alfa Slab One", serif;
    font-size: 52px;
    fill: var(--ink);
  }
  .product-name {
    font-family: "Lobster", cursive;
    font-size: 100px;
    fill: var(--ink);
  }
  .product-type {
    font-family: "Lobster", cursive;
    font-size: 74px;
    fill: var(--ink);
  }
  .since {
    font-family: "Playfair Display", serif;
    font-style: italic;
    font-size: 28px;
    fill: var(--ink);
  }
  .spec {
    font-family: "Open Sans", sans-serif;
    font-weight: 300;
    font-size: 21px;
    fill: var(--ink-soft);
  }
</style>
</head>
<body>
<main class="canvas">
  <svg class="label-art" viewBox="0 0 1200 1002" xmlns="http://www.w3.org/2000/svg" aria-labelledby="labelTitle">
    <title id="labelTitle">Osric's Hard Root Beer label</title>
    <defs>
      <path id="labelShape" d="M290 220 A55 55 0 0 0 345 165 C420 40 780 40 855 165 A55 55 0 0 0 910 220 L910 900 A55 55 0 0 0 855 955 L345 955 A55 55 0 0 0 290 900 Z"/>
      <clipPath id="labelClip"><use href="#labelShape"/></clipPath>
      <radialGradient id="sunburstGlow" cx="600" cy="560" r="520" gradientUnits="userSpaceOnUse">
        <stop offset="0" stop-color="#fdf9f5"/>
        <stop offset="0.55" stop-color="#fae6d8"/>
        <stop offset="1" stop-color="#f6d2ba"/>
      </radialGradient>
      <path id="kickerArc" d="M455 138 Q600 60 745 138"/>
      <path id="starShape" d="M0 -10 L2.9 -3.1 L9.5 -3.1 L4.2 1.2 L5.9 8.1 L0 4 L-5.9 8.1 L-4.2 1.2 L-9.5 -3.1 L-2.9 -3.1 Z"/>
    </defs>

    <!-- Label body -->
    <use href="#labelShape" class="label-body"/>
    <rect class="sunburst" x="280" y="20" width="640" height="945" clip-path="url(#labelClip)" role="img" aria-label="Soft peach sunburst rays radiating from the centre of the label"/>
    <use href="#labelShape" class="label-inner-rule" transform="translate(600 490) scale(0.965) translate(-600 -490)"/>

    <!-- Header -->
    <text class="kicker"><textPath href="#kickerArc" startOffset="50%" text-anchor="middle">GUARANTEED</textPath></text>

    <g class="star-row">
      <use href="#starShape" class="star" transform="translate(482 199) scale(0.8)"/>
      <use href="#starShape" class="star" transform="translate(510 199) scale(0.8)"/>
      <use href="#starShape" class="star" transform="translate(538 199) scale(0.8)"/>
      <use href="#starShape" class="star" transform="translate(600 196) scale(1.6)"/>
      <use href="#starShape" class="star" transform="translate(662 199) scale(0.8)"/>
      <use href="#starShape" class="star" transform="translate(690 199) scale(0.8)"/>
      <use href="#starShape" class="star" transform="translate(718 199) scale(0.8)"/>
    </g>

    <rect class="flourish" x="320" y="296" width="205" height="34" rx="17" role="img" aria-label="Vintage scroll flourish"/>
    <rect class="flourish" x="675" y="296" width="205" height="34" rx="17" role="img" aria-label="Vintage scroll flourish"/>
    <text class="category" x="600" y="334" text-anchor="middle">BEER</text>

    <!-- Name -->
    <text class="product-name" x="600" y="512" text-anchor="middle">Osric’s Hard</text>

    <!-- Ribbon -->
    <g class="ribbon">
      <path class="ribbon-tail" d="M220 622 L330 622 L330 734 L220 734 L262 678 Z"/>
      <path class="ribbon-tail" d="M870 622 L980 622 L938 678 L980 734 L870 734 Z"/>
      <path class="ribbon-fold" d="M306 672 L330 672 L330 700 Z"/>
      <path class="ribbon-fold" d="M894 672 L870 672 L870 700 Z"/>
      <path class="ribbon-band" d="M300 574 Q600 562 900 574 L894 674 Q600 662 306 674 Z"/>
    </g>
    <text class="product-type" x="600" y="646" text-anchor="middle">Root Beer</text>

    <!-- Footer -->
    <line class="rule" x1="446" y1="775" x2="506" y2="775"/>
    <line class="rule" x1="694" y1="775" x2="754" y2="775"/>
    <text class="since" x="600" y="785" text-anchor="middle">Since 2016</text>

    <text class="spec" x="388" y="897">355ml</text>
    <text class="spec" x="813" y="897" text-anchor="end">5,9% alc.</text>
  </svg>
</main>
</body>
</html>
```